Project Planning & Communication Process

Need a PowerPoint slide that illustrates our project planning and communication cycle. Our company has key meetings, and key communication vehicles (like emails and follow up tools) that we use to ensure our frontline staff are prepared to execute the new project successfully. This document needs to call out how the different components, like the meetings and emails, work together (like a flow chart), so someone who needs to use this process will understand what they should do. The slide needs to be simple yet comprehensive enough to guide someone through the details. I don't want it overwhelming. The primary focus is the process, not the details.

Use the color pallette included within the slide (shades of blue and gray, and black). This is for an insurance company (www.harborquill.com). Use this as a reference for the look and feel.

I have attached a sample slide of the flow chart process.

Click here if you cannot access the file. https://www.filecrate.example/s/q8wz2mbt7ypnc4r/Communcation_Methods_V1.pptx

If you are not able to see the uploaded slide.  Please send me your email address and I will send the slide to you directly. 

ISince I'm not able to upload the reference ppt file, 've uploaded the slide at FileCrate.  Please click here to access.
https://www.filecrate.example/s/q8wz2mbt7ypnc4r/Communcation_Methods_V1.pptx

Reason: extending one more day for designers to make last minute updates.

Target Market(s)

Vice Presidents and project managers/business partners within the organization.

Industry/Entity Type

Communication

Font styles to use
Sans Serif

Colors
3176b5

Requirements
Must have
• 1 page, color pallette assigned, be simple yet comprehensive. the focus needs to be on the process, not on the details.
Nice to have
• Doesn't have to follow the example I provided. Please feel free to approach from different ways.

```html
<!DOCTYPE html>
<html lang="en">
<head>
<meta charset="utf-8">
<title>Project Alignment &amp; Communication Process</title>
<link href="https://fonts.googleapis.com/css2?family=Archivo+Black&family=Archivo:wght@800&display=swap" rel="stylesheet">
<style>
  :root {
    --brand-blue: #3176b5;
    --ink: #262626;
    --paper: #ffffff;
    --shadow: rgba(0, 0, 0, 0.55);
  }
  html, body {
    margin: 0;
    padding: 0;
    width: 1200px;
    height: 900px;
    overflow: hidden;
    background: var(--paper);
  }
  .process-slide {
    display: block;
    width: 1200px;
    height: 900px;
  }
  .title {
    font-family: "Archivo Black", "Arial Black", sans-serif;
    fill: var(--ink);
    font-size: 38px;
  }
  .title-amp {
    font-family: "Archivo Black", "Arial Black", sans-serif;
    fill: var(--ink);
    font-size: 92px;
  }
  .stage-shape { fill: var(--ink); }
  .numeral {
    font-family: "Archivo Black", "Arial Black", sans-serif;
    fill: var(--brand-blue);
  }
  .numeral-shape { fill: var(--brand-blue); }
  .stage-name {
    font-family: "Archivo Black", "Arial Black", sans-serif;
    fill: var(--paper);
    font-size: 21px;
    filter: drop-shadow(2px 2px 1px var(--shadow));
  }
  .item {
    font-family: "Archivo", "Arial", sans-serif;
    font-weight: 800;
    fill: var(--paper);
    font-size: 15px;
    letter-spacing: 0.3px;
  }
  .item-large {
    font-family: "Archivo Black", "Arial Black", sans-serif;
    fill: var(--paper);
    font-size: 21px;
  }
  .timing-arrow { fill: var(--paper); }
  .timing-label {
    font-family: "Archivo", "Arial", sans-serif;
    font-weight: 800;
    fill: var(--brand-blue);
    font-size: 14.5px;
  }
</style>
</head>
<body>
<svg class="process-slide" viewBox="0 0 1080 810" xmlns="http://www.w3.org/2000/svg" aria-labelledby="slide-title">
  <defs>
    <clipPath id="below-title">
      <rect x="0" y="130" width="1080" height="700"/>
    </clipPath>
    <clipPath id="canvas">
      <rect x="0" y="0" width="1080" height="810"/>
    </clipPath>
  </defs>

  <g clip-path="url(#canvas)">
    <!-- top accent -->
    <polygon class="stage-shape" points="760,0 980,0 993,20 748,20"/>

    <!-- stage backdrops -->
    <g class="stage-backdrops" clip-path="url(#below-title)">
      <ellipse class="stage-shape" cx="176" cy="470" rx="172" ry="345"/>
      <ellipse class="stage-shape" cx="572" cy="545" rx="172" ry="380"/>
      <ellipse class="stage-shape" cx="906" cy="380" rx="178" ry="315"/>
    </g>

    <!-- stage numerals -->
    <path class="numeral-shape" d="M110 728 L270 732 L302 150 L182 150 L0 278 L0 408 L126 348 Z"/>
    <text class="numeral" x="385" y="838" font-size="600" transform="rotate(-8 580 600)">2</text>
    <text class="numeral" x="690" y="462" font-size="530" transform="rotate(-14 880 300)">3</text>

    <!-- title -->
    <text id="slide-title" class="title" x="38" y="74" textLength="445" lengthAdjust="spacingAndGlyphs">PROJECT ALIGNMENT</text>
    <text class="title" x="38" y="108" textLength="560" lengthAdjust="spacingAndGlyphs">COMMUNICATION PROCESS</text>
    <text class="title-amp" x="490" y="72" textLength="88" lengthAdjust="spacingAndGlyphs">&amp;</text>

    <!-- stage 1 : plan & design -->
    <g class="stage stage-plan">
      <text class="stage-name" text-anchor="middle" x="80" y="288">PLAN</text>
      <text class="stage-name" text-anchor="middle" x="80" y="310">&amp;</text>
      <text class="stage-name" text-anchor="middle" x="82" y="333">DESIGN</text>

      <polygon class="timing-arrow" points="148,164 236,164 236,144 300,178 236,212 236,193 148,193"/>
      <text class="timing-label" x="166" y="184">3+ MONTHS OUT</text>

      <g class="item" text-anchor="end">
        <text x="300" y="229">NEW</text>
        <text x="300" y="251">PROJECT</text>
        <text x="300" y="296">IDENTIFIED</text>
        <text x="300" y="318">GOVERNANCE</text>
        <text x="300" y="341">MEETING</text>
        <text x="300" y="386">SEPARATE PROJECT</text>
        <text x="300" y="409">MEETINGS AS</text>
        <text x="300" y="431">NEEDED</text>
      </g>

      <polygon class="timing-arrow" points="52,444 140,444 140,424 220,458 140,492 140,473 52,473"/>
      <text class="timing-label" x="61" y="464">2 + MONTHS OUT</text>

      <g class="item">
        <text x="61" y="509">GOVERNANCE</text>
        <text x="61" y="531">MEETING</text>
        <text x="61" y="576">WEEKLY CENTER</text>
        <text x="61" y="598">LEADER</text>
        <text x="61" y="621">MEETING</text>
        <text x="61" y="666">FIELD ADVISORY</text>
        <text x="61" y="689">PANEL</text>
      </g>
    </g>

    <!-- stage 2 : prepare -->
    <g class="stage stage-prepare">
      <text class="stage-name" x="436" y="530" transform="rotate(-30 436 530)">PREPARE</text>

      <polygon class="timing-arrow" points="567,451 656,451 656,431 736,465 656,499 656,481 567,481"/>
      <text class="timing-label" x="600" y="472">1 MONTH OUT</text>

      <g class="item" text-anchor="end">
        <text x="726" y="543">WEEKLY CENTER</text>
        <text x="726" y="565">LEADER</text>
        <text x="728" y="588">MEETING</text>
      </g>

      <polygon class="timing-arrow" points="476,638 564,638 564,617 644,651 564,685 564,667 476,667"/>
      <text class="timing-label" x="485" y="658">1 WEEK OUT</text>

      <g class="item">
        <text x="486" y="702">MONDAY</text>
        <text x="486" y="725">MEMO</text>
        <text x="488" y="770">DAILY</text>
        <text x="488" y="793">DIGEST</text>
      </g>
    </g>

    <!-- stage 3 : follow up / evaluate -->
    <g class="stage stage-follow-up">
      <g transform="rotate(-22 810 140)">
        <text class="stage-name" x="742" y="140">FOLLOW UP/</text>
        <text class="stage-name" x="770" y="164">EVALUATE</text>
      </g>
      <g class="item-large" text-anchor="end">
        <text x="978" y="233" transform="rotate(-4 978 233)">FOLLOW</text>
        <text x="982" y="256">UP</text>
        <text x="982" y="280">GUIDE</text>
        <text x="985" y="320">POST</text>
        <text x="988" y="345" transform="rotate(-4 988 345)">LAUNCH</text>
      </g>
    </g>
  </g>
</svg>
</body>
</html>
```